Zielgruppe
Die travlon GmbH bietet professionelle Cloud-Lösungen im Bereich spezialisierter Verwaltungssysteme. Hierbei handelt es sich um Software as a Service (SaaS), die zu 100% von der travlon GmbH betrieben und kontinuierlich weiterentwickelt wird.
Aufgabenstellung
Das Design kann Farben und/oder Elemente der travlon GmbH enthalten (www.travlon.de). Da es sich um ein eigenen Produkt handelt, muss jedoch auch Neutralität bewahrt werden.

```html
<!DOCTYPE html>
<html lang="de">
<head>
<meta charset="utf-8">
<title>travlon – Anmeldung</title>
<link href="https://fonts.googleapis.com/css2?family=Lato:wght@400;700&display=swap" rel="stylesheet">
<style>
  :root {
    --bg-light: #b6c6d4;
    --bg-mid: #9cb0c3;
    --bg-dark: #4a6380;
    --bg-deep: #405873;
    --accent: #d0003c;
    --card: #ffffff;
    --line: #cfd3d8;
    --text: #4a5560;
    --muted: #7a8aa0;
    --field: #f1f1f1;
    --field-border: #c9c9c9;
  }
  * { margin: 0; padding: 0; box-sizing: border-box; }
  html, body { width: 1200px; height: 731px; overflow: hidden; }
  body { font-family: "Lato", sans-serif; color: var(--text); }
  .stage { position: relative; width: 1200px; height: 731px; overflow: hidden; }
  .backdrop {
    position: absolute; inset: 0;
    background: linear-gradient(90deg, var(--bg-light) 0%, var(--bg-light) 30%, var(--bg-mid) 50%, var(--bg-dark) 75%, var(--bg-deep) 100%);
  }
  .login-card {
    position: absolute; left: 305px; top: 216px; width: 590px; height: 284px;
    background: var(--card); border-radius: 4px;
  }
  .login-fieldset {
    position: absolute; left: 30px; top: 42px; width: 530px; height: 195px;
    border: 1px solid var(--line); border-radius: 3px;
  }
  .login-legend {
    position: absolute; left: 17px; top: -12px; padding: 0 11px;
    background: var(--card); font-size: 14px; line-height: 20px;
  }
  .field-label { position: absolute; left: 59px; font-size: 11.5px; line-height: 14px; }
  .field-input {
    position: absolute; left: 170px; width: 248px; height: 26px;
    background: var(--field); border: 1px solid var(--field-border); border-radius: 13px;
    font-size: 10px; line-height: 24px; padding-left: 18px; color: #777;
  }
  .field-input.password { letter-spacing: 1px; font-size: 11px; }
  .reveal-icon { position: absolute; left: 425px; top: 87px; }
  .submit-btn {
    position: absolute; left: 173px; top: 117px; width: 115px; height: 25px;
    background: var(--accent); color: #fff; border-radius: 13px;
    font-size: 11px; font-weight: 700; line-height: 25px; text-align: center;
  }
  .forgot-link {
    position: absolute; right: 31px; top: 245px; font-size: 11.5px; color: var(--muted);
  }
</style>
</head>
<body>
<main class="stage">
  <div class="backdrop" role="img" aria-label="Dekorativer Hintergrund mit geschwungenen Bändern und Wabenmuster"></div>

  <section class="login-card">
    <div class="login-fieldset">
      <span class="login-legend">Anmeldebereich</span>
      <span class="field-label" style="top:54px">Benutzername:</span>
      <div class="field-input" style="top:47px">Loginseite</div>
      <span class="field-label" style="top:87px">Passwort:</span>
      <div class="field-input password" style="top:79px">•••••••••••</div>
      <svg class="reveal-icon" width="18" height="12" viewBox="0 0 18 12" aria-label="Passwort anzeigen">
        <path d="M1,6 C4,1 14,1 17,6 C14,11 4,11 1,6 Z" fill="none" stroke="#555" stroke-width="1.2"/>
        <circle cx="9" cy="6" r="2.6" fill="#555"/>
      </svg>
      <div class="submit-btn">Anmelden</div>
    </div>
    <span class="forgot-link">Passwort vergessen?</span>
  </section>
</main>
</body>
</html>
```